Harborline Network Advisors (HNA) Business Card

Front Side, add Company Logo
1.) Harborline Network Advisors
Director of Operations
Delgado, Marco T
(323) 555 0148
782 n Alder Ave Suite 300 PMB2093
Los Angeles, CA 90013
Marco@HarborlineNA.example
www.HarborlineNA.example
2.) Veteran-Owned Business (with Small EGA)

Back Side
- Pictures are ideas of what you can add. The description is what HNA does.
1.) Business Partners:
- Corvalis Business
- KX&L Business
- Tellmora Business
2.) What we do
- Broker of Internet service (partners above)
- Project Management/ Contract Management
- Government Contracts

```html
<!DOCTYPE html>
<html lang="en">
<head>
<meta charset="utf-8">
<title>Harborline Network Advisors – Business Card</title>
<link rel="stylesheet" href="https://fonts.googleapis.com/css2?family=Poppins:wght@400;500;600;700&display=swap">
<style>
  :root {
    --page: #e6e6e6;
    --ink: #1f1c1d;
    --charcoal: #231f20;
    --gold: #f9b51c;
    --paper: #ffffff;
    --paper-soft: #f5f5f5;
    --muted: #3a3a3a;
    --rule: #9a9a9a;
    --rack-dark: #1b2030;
    --rack-blue: #4a5fa8;
  }
  * { box-sizing: border-box; margin: 0; padding: 0; }
  html, body {
    width: 686px; height: 1200px; overflow: hidden;
    background: var(--page);
    font-family: "Poppins", sans-serif;
    color: var(--ink);
  }
  .canvas { position: relative; width: 686px; height: 1200px; }
  .card {
    position: absolute; left: 33px; width: 620px; height: 354px;
    overflow: hidden; background: var(--paper);
    box-shadow: 0 4px 14px rgba(0,0,0,.18);
  }
  .card--front { top: 221px; background: var(--paper-soft); }
  .card--back { top: 625px; }
  .card__art { position: absolute; inset: 0; width: 620px; height: 354px; }

  /* Front: brand mark */
  .brand-mark {
    position: absolute; left: 44px; top: 112px; width: 190px;
    display: flex; flex-direction: column; align-items: center; gap: 10px;
    color: var(--gold); font-weight: 600; text-align: center;
  }
  .brand-mark__dot { width: 34px; height: 34px; border-radius: 50%; background: var(--gold); }
  .brand-mark__name { font-size: 19px; line-height: 1.2; letter-spacing: .5px; }

  /* Front: contact block */
  .contact { position: absolute; left: 340px; top: 50px; width: 262px; }
  .contact__company { font-size: 15.5px; font-weight: 500; white-space: nowrap; }
  .contact__name { font-size: 22px; font-weight: 700; line-height: 1.2; margin-top: 6px; white-space: nowrap; }
  .contact__name em { font-style: normal; color: var(--gold); }
  .contact__title { font-size: 12px; color: var(--muted); }
  .contact__rule { height: 1px; background: var(--rule); margin: 8px 0 10px; }
  .contact__list { list-style: none; font-size: 12px; line-height: 1.35; }
  .contact__item { display: flex; align-items: flex-start; gap: 9px; margin-bottom: 8px; white-space: nowrap; }
  .contact__icon { flex: none; width: 14px; height: 14px; margin-top: 1px; }
  .veteran { position: absolute; left: 345px; top: 280px; font-size: 12px; color: var(--muted); }
  .veteran-emblem {
    position: absolute; left: 513px; top: 265px; width: 40px; height: 44px;
    border-radius: 50%; background: radial-gradient(circle, #d9d9d9, #c4c4c4);
  }

  /* Back: services */
  .services { position: absolute; left: 35px; top: 32px; color: var(--paper); }
  .services__heading { font-size: 21px; font-weight: 400; letter-spacing: .3px; }
  .services__heading strong { color: var(--gold); font-weight: 700; }
  .services__list { list-style: none; margin-top: 12px; }
  .services__item { display: flex; gap: 8px; font-size: 14.5px; font-weight: 600; line-height: 1.25; margin-bottom: 15px; }
  .services__item span { display: block; font-weight: 400; }
  .services__icon { flex: none; width: 16px; height: 16px; margin-top: 2px; }

  .rack-photo {
    position: absolute; left: 340px; top: 0; width: 280px; height: 271px;
    background: linear-gradient(180deg, var(--rack-dark) 0%, #39405a 35%, var(--rack-blue) 60%, #2a2f44 100%);
  }
  .partners {
    position: absolute; left: 0; top: 271px; width: 620px; height: 83px;
    background: var(--paper); display: flex; align-items: center;
  }
  .partners__label { position: absolute; left: 35px; font-size: 15.5px; font-weight: 500; letter-spacing: 1.8px; }
  .partners__name {
    position: absolute; font-size: 11.5px; font-weight: 600; color: var(--ink);
    transform: translateX(-50%); white-space: nowrap;
  }
</style>
</head>
<body>
<main class="canvas">

  <!-- Front side -->
  <section class="card card--front" aria-label="Business card front">
    <svg class="card__art" viewBox="0 0 620 354" aria-hidden="true">
      <circle cx="20" cy="40" r="316.5" fill="var(--gold)"/>
      <circle cx="0" cy="125" r="304" fill="var(--charcoal)"/>
    </svg>

    <div class="brand-mark">
      <span class="brand-mark__dot"></span>
      <span class="brand-mark__name">Harborline<br>Network<br>Advisors</span>
    </div>

    <div class="contact">
      <p class="contact__company">Harborline Network Advisors</p>
      <p class="contact__name">Delgado, <em>Marco T</em></p>
      <p class="contact__title">Director of Operations</p>
      <div class="contact__rule"></div>
      <ul class="contact__list">
        <li class="contact__item">
          <svg class="contact__icon" viewBox="0 0 14 14"><rect width="14" height="14" rx="2" fill="var(--gold)"/><path d="M4 3.5l1.6-.3 1 2-1 .8a5 5 0 0 0 2.4 2.4l.8-1 2 1-.3 1.6C7.5 10.3 3.7 6.5 4 3.5z" fill="var(--charcoal)"/></svg>
          <span>(323) 555 0148</span>
        </li>
        <li class="contact__item">
          <svg class="contact__icon" viewBox="0 0 14 14"><rect width="14" height="14" rx="2" fill="var(--gold)"/><path d="M7 2.5a3 3 0 0 1 3 3c0 2.2-3 5.8-3 5.8S4 7.7 4 5.5a3 3 0 0 1 3-3z" fill="var(--charcoal)"/><circle cx="7" cy="5.5" r="1.1" fill="var(--gold)"/></svg>
          <span>782 n Alder Ave Suite 300 PMB2093<br>Los Angeles, CA 90013</span>
        </li>
        <li class="contact__item">
          <svg class="contact__icon" viewBox="0 0 14 14"><rect width="14" height="14" rx="2" fill="var(--gold)"/><rect x="3" y="4" width="8" height="6" fill="var(--charcoal)"/><path d="M3 4l4 3.2L11 4" stroke="var(--gold)" stroke-width="1" fill="none"/></svg>
          <span>Marco@HarborlineNA.example</span>
        </li>
        <li class="contact__item">
          <svg class="contact__icon" viewBox="0 0 14 14"><rect width="14" height="14" rx="2" fill="var(--gold)"/><circle cx="7" cy="7" r="3.8" fill="none" stroke="var(--charcoal)" stroke-width="1.1"/><path d="M3.2 7h7.6M7 3.2c-2 2.2-2 5.4 0 7.6M7 3.2c2 2.2 2 5.4 0 7.6" stroke="var(--charcoal)" stroke-width=".9" fill="none"/></svg>
          <span>www.HarborlineNA.example</span>
        </li>
      </ul>
    </div>

    <p class="veteran">Veteran-Owned Business</p>
    <div class="veteran-emblem" role="img" aria-label="Small veteran service emblem"></div>
  </section>

  <!-- Back side -->
  <section class="card card--back" aria-label="Business card back">
    <div class="rack-photo" role="img" aria-label="Photo of a network server rack with blue patch cables"></div>
    <svg class="card__art" viewBox="0 0 620 354" aria-hidden="true">
      <circle cx="149" cy="24" r="333" fill="var(--gold)"/>
      <circle cx="178" cy="12" r="279" fill="var(--paper)"/>
      <circle cx="178" cy="12" r="270" fill="var(--charcoal)"/>
    </svg>

    <div class="services">
      <h2 class="services__heading"><strong>WHAT</strong> WE DO</h2>
      <ul class="services__list">
        <li class="services__item">
          <svg class="services__icon" viewBox="0 0 16 16"><circle cx="8" cy="8" r="6" fill="none" stroke="var(--gold)" stroke-width="1.4"/><path d="M2 8h12M8 2c-2.6 3-2.6 9 0 12M8 2c2.6 3 2.6 9 0 12" stroke="var(--gold)" stroke-width="1.1" fill="none"/></svg>
          <div>Broker of Internet service<span>(partners below)</span></div>
        </li>
        <li class="services__item">
          <svg class="services__icon" viewBox="0 0 16 16"><rect x="2.5" y="1.5" width="11" height="13" rx="1" fill="none" stroke="var(--gold)" stroke-width="1.4"/><path d="M5 5h6M5 8h6M5 11h4" stroke="var(--gold)" stroke-width="1.2"/></svg>
          <div>Project Management/<br>Contract Management</div>
        </li>
        <li class="services__item">
          <svg class="services__icon" viewBox="0 0 16 16"><path d="M1.5 6L8 2l6.5 4z" fill="var(--gold)"/><path d="M3 7v6M6.3 7v6M9.7 7v6M13 7v6M1.5 14.3h13" stroke="var(--gold)" stroke-width="1.4"/></svg>
          <div>Government Contracts</div>
        </li>
      </ul>
    </div>

    <div class="partners">
      <p class="partners__label">Business Partners</p>
      <p class="partners__name" style="left:311px">Corvalis Business</p>
      <p class="partners__name" style="left:434px">KX&amp;L Business</p>
      <p class="partners__name" style="left:541px">Tellmora Business</p>
    </div>
  </section>

</main>
</body>
</html>
```